Real estate company needs a card that makes you say WOW!

We need an awesome business card for our real estate company, Keystone Realty Group of Chicago, that will stand out from the crowd. We specialize in buying and selling real estate, property management, and real estate investments (Flips & Rentals). On the business card, I need the following:

- Our logo
- Services
- My name & contact info (Derek Holloway, 630-517-2946, Derek@KeystoneChi.example)
- My title (Director of Acquisitions)
- KeystoneChi.example

I attached an EPS file of our logo. Let me know if you have any questions. Thank you in advance!

```html
<!DOCTYPE html>
<html lang="en">
<head>
<meta charset="utf-8">
<title>Keystone Realty Group of Chicago – Business Card</title>
<link rel="stylesheet" href="https://fonts.googleapis.com/css2?family=Tinos:wght@400;700&display=swap">
<style>
  :root {
    --backdrop: #e9eef2;
    --card: #ffffff;
    --brand-blue: #1f6fb7;
    --accent-blue: #2a8fd8;
    --text-grey: #4d4d4d;
    --text-dark: #2b2b2b;
    --bar-dark: #2f3235;
    --faint: #f6f7f8;
  }
  * { box-sizing: border-box; margin: 0; padding: 0; }
  html, body {
    width: 1200px; height: 965px; overflow: hidden;
    background: var(--backdrop);
    font-family: "Tinos", "Times New Roman", serif;
  }
  .canvas { position: relative; width: 1200px; height: 965px; }
  .card {
    position: absolute; width: 648px; height: 366px;
    background: var(--card); overflow: hidden;
  }
  .card--front { left: 286px; top: 75px; }
  .card--back { left: 285px; top: 528px; }

  /* Front */
  .front-brand {
    position: absolute; top: 112px; left: 0; width: 100%;
    text-align: center; color: var(--text-dark);
    font-size: 24px; font-weight: 400;
  }
  .services-title {
    position: absolute; top: 172px; left: 0; width: 100%;
    text-align: center; color: var(--accent-blue);
    font-size: 21px; font-weight: 700; letter-spacing: .5px;
  }
  .services-list {
    position: absolute; top: 204px; left: 171px; list-style: none;
    color: var(--text-grey); font-size: 16px; line-height: 19.5px;
  }
  .services-list li { display: flex; align-items: center; gap: 7px; }
  .services-list li::before {
    content: ""; width: 7px; height: 7px; background: var(--brand-blue);
    border-radius: 2px 2px 0 0;
  }

  /* Back */
  .skyline-area {
    position: absolute; left: 320px; top: 40px; width: 328px; height: 310px;
    background: linear-gradient(to bottom, #ffffff, var(--faint) 40%, var(--faint));
  }
  .back-brand {
    position: absolute; top: 92px; left: 46px; width: 300px;
    color: var(--text-dark); font-size: 24px; font-weight: 400;
    line-height: 30px;
  }
  .person {
    position: absolute; top: 176px; right: 40px; text-align: right;
  }
  .person-name { color: var(--text-dark); font-size: 20px; font-weight: 700; }
  .person-title { color: var(--accent-blue); font-size: 15px; margin-top: 3px; }
  .tab {
    position: absolute; right: -22px; top: 177px;
    width: 44px; height: 44px; border-radius: 50%; background: var(--accent-blue);
  }
  .contacts {
    position: absolute; top: 245px; left: 46px; list-style: none;
    color: var(--text-grey); font-size: 14.5px; line-height: 20px;
  }
  .contacts li { display: flex; align-items: center; gap: 8px; }
  .contacts svg { width: 14px; height: 14px; flex: none; }
  .bar { position: absolute; bottom: 0; height: 16px; }
  .bar--dark { left: 0; width: 375px; background: var(--bar-dark);
    clip-path: polygon(0 0, 100% 0, 97% 100%, 0 100%); }
  .bar--blue { left: 355px; right: 0; background: var(--accent-blue);
    clip-path: polygon(4% 0, 100% 0, 100% 100%, 0 100%); }
</style>
</head>
<body>
<main class="canvas">
  <section class="card card--front">
    <div class="front-brand">Keystone Realty Group of Chicago</div>
    <h2 class="services-title">OUR SERVICE</h2>
    <ul class="services-list">
      <li>Property management</li>
      <li>Buying and selling real estate</li>
      <li>Real estate investments (Flips &amp; Rentals)</li>
    </ul>
  </section>

  <section class="card card--back">
    <div class="skyline-area" role="img" aria-label="Faint city skyline backdrop"></div>
    <div class="back-brand">Keystone Realty<br>Group of Chicago</div>
    <div class="person">
      <div class="person-name">Derek Holloway</div>
      <div class="person-title">Director of Acquisitions</div>
    </div>
    <div class="tab"></div>
    <ul class="contacts">
      <li>
        <svg viewBox="0 0 16 16" aria-hidden="true"><circle cx="8" cy="8" r="7" fill="none" stroke="#2a8fd8" stroke-width="1.5"/><path d="M5.5 4.5l1.3 0 .7 2-1 .8a5 5 0 0 0 2.2 2.2l.8-1 2 .7v1.3c0 .5-.5 1-1 1A6 6 0 0 1 4.5 5.5c0-.5.5-1 1-1z" fill="#2a8fd8"/></svg>
        630-517-2946
      </li>
      <li>
        <svg viewBox="0 0 16 16" aria-hidden="true"><rect x="1" y="3" width="14" height="10" fill="#2a8fd8"/><path d="M1 3l7 6 7-6" fill="none" stroke="#fff" stroke-width="1.3"/></svg>
        Derek@KeystoneChi.example
      </li>
      <li>
        <svg viewBox="0 0 16 16" aria-hidden="true"><circle cx="8" cy="8" r="7" fill="#2a8fd8"/><path d="M1 8h14M8 1v14M8 1c-3 3-3 11 0 14M8 1c3 3 3 11 0 14" fill="none" stroke="#fff" stroke-width="1"/></svg>
        www.keystonechi.example
      </li>
    </ul>
    <div class="bar bar--dark"></div>
    <div class="bar bar--blue"></div>
  </section>
</main>
</body>
</html>
```